PLUMBING VAN WRAP DESIGN - HARROWFIELD MECHANICAL

i have logos and basic layout for what the van wrap should look like. Everything in place can be moved around and adjusted. We want this look modern and professional. We do not want any sort of cartoon figures or any sort. The customer works on plumbing and heating and fire and ice is represented in the logo so maybe it can have that sort of feel to it. we are very open to suggestions for the final product. The logos and the slogans are import to the customer so please be as creative as you can with it.

```html
<!DOCTYPE html>
<html lang="en">
<head>
<meta charset="utf-8">
<title>Harrowfield Mechanical – Van Wrap Layout</title>
<link rel="stylesheet" href="https://fonts.googleapis.com/css2?family=Archivo+Black&family=Roboto:wght@300;400&display=swap">
<style>
  :root {
    --navy: #1f2a7a;
    --gold: #d9a21b;
    --silver: #dfe2e8;
    --silver-light: #f4f5f8;
    --white: #ffffff;
    --page: #ffffff;
    --ink: #1c2a8c;
    --ice: #4a8fe0;
  }
  * { box-sizing: border-box; margin: 0; padding: 0; }
  html, body { width: 849px; height: 1200px; overflow: hidden; background: var(--page); }
  .sheet { position: relative; width: 849px; height: 1200px; }

  .panel { position: absolute; }
  .panel svg.wrap-art { position: absolute; inset: 0; width: 100%; height: 100%; }
  .panel--driver { left: 65px; top: 60px; width: 720px; height: 280px; }
  .panel--passenger { left: 65px; top: 410px; width: 720px; height: 280px; }
  .panel--front { left: 75px; top: 770px; width: 320px; height: 380px; }
  .panel--rear { left: 465px; top: 770px; width: 300px; height: 380px; }
  .panel--passenger svg.wrap-art { transform: scaleX(-1); }

  .brand-mark {
    position: absolute;
    border-radius: 50%;
    background: var(--ice);
  }

  .tagline {
    position: absolute;
    font-family: "Archivo Black", sans-serif;
    font-size: 11px; line-height: 13px;
    color: var(--white); letter-spacing: 0.4px;
  }
  .services { position: absolute; list-style: none; font-family: "Roboto", sans-serif; font-weight: 300; color: var(--white); }
  .services li::before { content: "•"; margin-right: 4px; font-weight: 400; }
  .panel--driver .services, .panel--passenger .services { font-size: 17px; line-height: 20px; }

  .brand-name {
    position: absolute; text-align: center;
    font-family: "Archivo Black", sans-serif; color: var(--white);
  }
  .brand-name .name-main { display: block; }
  .brand-name .name-sub { display: block; letter-spacing: 1.5px; }
  .panel--driver .brand-name, .panel--passenger .brand-name { width: 230px; }
  .panel--driver .brand-name .name-main, .panel--passenger .brand-name .name-main { font-size: 26px; line-height: 30px; }
  .panel--driver .brand-name .name-sub, .panel--passenger .brand-name .name-sub { font-size: 12px; line-height: 16px; }
  .brand-rule { position: absolute; height: 2px; background: var(--ice); }

  .phone {
    position: absolute; font-family: "Archivo Black", sans-serif;
    color: var(--ink); text-align: center; letter-spacing: 0.5px;
  }
  .panel--driver .phone, .panel--passenger .phone { font-size: 32px; line-height: 36px; width: 300px; }

  .panel--front .brand-name { left: 60px; top: 190px; width: 200px; }
  .panel--front .brand-name .name-main { font-size: 15px; line-height: 17px; }
  .panel--front .brand-name .name-sub { font-size: 7px; line-height: 9px; }

  .panel--rear .brand-name { left: 20px; top: 95px; width: 260px; }
  .panel--rear .brand-name .name-main { font-size: 24px; line-height: 28px; }
  .panel--rear .brand-name .name-sub { font-size: 12px; line-height: 16px; }
  .panel--rear .services { left: 70px; top: 160px; font-size: 15px; line-height: 18px; }
  .panel--rear .phone { left: 0; top: 283px; width: 300px; font-size: 25px; line-height: 30px; }
</style>
</head>
<body>
<main class="sheet">

  <!-- Driver side -->
  <section class="panel panel--driver" aria-label="Driver side wrap">
    <svg class="wrap-art" viewBox="0 0 720 280" preserveAspectRatio="none" aria-hidden="true">
      <defs>
        <clipPath id="side-clip-a"><rect width="720" height="280" rx="30"/></clipPath>
        <linearGradient id="silver-a" x1="0" y1="0" x2="0" y2="1">
          <stop offset="0" stop-color="#f4f5f8"/><stop offset="1" stop-color="#dfe2e8"/>
        </linearGradient>
      </defs>
      <g clip-path="url(#side-clip-a)">
        <rect width="720" height="280" fill="#1f2a7a"/>
        <path d="M40,280 L78,192 Q86,176 104,176 L690,176 Q708,176 720,150 L720,166 Q710,190 692,190 L112,190 Q98,190 92,204 L60,280 Z" fill="#d9a21b"/>
        <path d="M60,280 L92,204 Q98,190 112,190 L692,190 Q710,190 720,166 L720,280 Z" fill="url(#silver-a)"/>
      </g>
    </svg>
    <p class="tagline" style="left:80px; top:62px;">BIG ENOUGH TO HELP<br>SMALL ENOUGH TO CARE</p>
    <ul class="services" style="left:72px; top:92px;">
      <li>PLUMBING</li><li>HEATING</li><li>AIR CONDITIONING</li>
    </ul>
    <div class="brand-mark" role="img" aria-label="Harrowfield Mechanical brand mark" style="left:428px; top:44px; width:54px; height:54px;"></div>
    <div class="brand-rule" style="left:340px; top:112px; width:230px;"></div>
    <p class="brand-name" style="left:340px; top:118px;">
      <span class="name-main">HARROWFIELD</span>
      <span class="name-sub">MECHANICAL LLC</span>
    </p>
    <div class="brand-rule" style="left:340px; top:168px; width:230px;"></div>
    <p class="phone" style="left:300px; top:205px;">907-555-0142</p>
  </section>

  <!-- Passenger side -->
  <section class="panel panel--passenger" aria-label="Passenger side wrap">
    <svg class="wrap-art" viewBox="0 0 720 280" preserveAspectRatio="none" aria-hidden="true">
      <defs>
        <clipPath id="side-clip-b"><rect width="720" height="280" rx="30"/></clipPath>
        <linearGradient id="silver-b" x1="0" y1="0" x2="0" y2="1">
          <stop offset="0" stop-color="#f4f5f8"/><stop offset="1" stop-color="#dfe2e8"/>
        </linearGradient>
      </defs>
      <g clip-path="url(#side-clip-b)">
        <rect width="720" height="280" fill="#1f2a7a"/>
        <path d="M40,280 L78,192 Q86,176 104,176 L690,176 Q708,176 720,150 L720,166 Q710,190 692,190 L112,190 Q98,190 92,204 L60,280 Z" fill="#d9a21b"/>
        <path d="M60,280 L92,204 Q98,190 112,190 L692,190 Q710,190 720,166 L720,280 Z" fill="url(#silver-b)"/>
      </g>
    </svg>
    <div class="brand-mark" role="img" aria-label="Harrowfield Mechanical brand mark" style="left:358px; top:44px; width:54px; height:54px;"></div>
    <div class="brand-rule" style="left:270px; top:112px; width:230px;"></div>
    <p class="brand-name" style="left:270px; top:118px;">
      <span class="name-main">HARROWFIELD</span>
      <span class="name-sub">MECHANICAL LLC</span>
    </p>
    <div class="brand-rule" style="left:270px; top:168px; width:230px;"></div>
    <p class="tagline" style="left:530px; top:62px;">BIG ENOUGH TO HELP<br>SMALL ENOUGH TO CARE</p>
    <ul class="services" style="left:522px; top:92px;">
      <li>PLUMBING</li><li>HEATING</li><li>AIR CONDITIONING</li>
    </ul>
    <p class="phone" style="left:230px; top:205px;">907-555-0142</p>
  </section>

  <!-- Front -->
  <section class="panel panel--front" aria-label="Front wrap">
    <svg class="wrap-art" viewBox="0 0 320 380" preserveAspectRatio="none" aria-hidden="true">
      <defs><clipPath id="front-clip"><rect width="320" height="380" rx="34"/></clipPath></defs>
      <g clip-path="url(#front-clip)">
        <rect width="320" height="380" fill="#1f2a7a"/>
        <path d="M0,288 Q160,278 320,288 L320,296 Q160,286 0,296 Z" fill="#d9a21b"/>
        <path d="M0,296 Q160,286 320,296 L320,380 L0,380 Z" fill="#ffffff"/>
      </g>
    </svg>
    <div class="brand-mark" role="img" aria-label="Harrowfield Mechanical brand mark" style="left:148px; top:164px; width:24px; height:24px;"></div>
    <p class="brand-name">
      <span class="name-main">HARROWFIELD</span>
      <span class="name-sub">MECHANICAL LLC</span>
    </p>
  </section>

  <!-- Rear -->
  <section class="panel panel--rear" aria-label="Rear wrap">
    <svg class="wrap-art" viewBox="0 0 300 380" preserveAspectRatio="none" aria-hidden="true">
      <defs><clipPath id="rear-clip"><rect width="300" height="380" rx="24"/></clipPath></defs>
      <g clip-path="url(#rear-clip)">
        <rect width="300" height="380" fill="#1f2a7a"/>
        <path d="M0,262 Q150,246 300,254 L300,262 Q150,254 0,270 Z" fill="#d9a21b"/>
        <path d="M0,270 Q150,254 300,262 L300,380 L0,380 Z" fill="#ffffff"/>
      </g>
    </svg>
    <div class="brand-mark" role="img" aria-label="Harrowfield Mechanical brand mark" style="left:122px; top:28px; width:56px; height:56px;"></div>
    <div class="brand-rule" style="left:25px; top:89px; width:250px;"></div>
    <p class="brand-name">
      <span class="name-main">HARROWFIELD</span>
      <span class="name-sub">MECHANICAL LLC</span>
    </p>
    <ul class="services">
      <li>PLUMBING</li><li>HEATING</li><li>AIR CONDITIONING</li>
    </ul>
    <p class="phone">907-555-0142</p>
  </section>

</main>
</body>
</html>
```